Design my Company Letterhead

Hi there,
I need a letterhead built for my company. This means a company logo and details at the top of a letter - I want to be able to print it out in A4 size.

It needs to:
1) Look good - professional and matching my logo & colours
2) Contain my company logo (attached)
3) Contain these details:
Email: studio@harborlumenworks.com
Phone: +44 141 782 3094
Address:
47 Thornbury Lane
Office 14, Suite #58207
Leeds, West Yorkshire
United Kingdom

Make it interesting! We're a design studio so we can afford to be a little bit creative. It still needs to feel professional though.

```html
<!DOCTYPE html>
<html lang="en">
<head>
<meta charset="utf-8">
<title>Harbor Lumen Works — Letterhead</title>
<link rel="stylesheet" href="https://fonts.googleapis.com/css2?family=Arimo:wght@400&family=Tinos:wght@400&display=swap">
<style>
  :root {
    --brand-blue: #1b74bf;
    --brand-blue-dark: #135a96;
    --shadow-grey: #d9dde2;
    --paper: #ffffff;
    --ink: #1a1a1a;
    --ink-soft: #444444;
  }
  html, body {
    margin: 0;
    padding: 0;
    width: 858px;
    height: 1200px;
    overflow: hidden;
    background: var(--paper);
  }
  .letterhead {
    position: relative;
    width: 858px;
    height: 1200px;
    background: var(--paper);
    color: var(--ink);
    font-family: "Arimo", Arial, sans-serif;
  }
  .header-band {
    position: absolute;
    top: 0;
    left: 0;
    width: 858px;
    height: 90px;
  }
  .contact {
    position: absolute;
    right: 40px;
    top: 38px;
    text-align: right;
    font-size: 12.5px;
    line-height: 22px;
    color: var(--ink);
  }
  .date-line {
    position: absolute;
    right: 100px;
    top: 140px;
    font-size: 14px;
    letter-spacing: 0.5px;
  }
  .brand {
    position: absolute;
    left: 60px;
    top: 178px;
    display: flex;
    align-items: center;
    gap: 12px;
  }
  .brand-mark {
    width: 22px;
    height: 22px;
    border-radius: 50%;
    background: var(--brand-blue);
  }
  .brand-name {
    font-family: "Tinos", "Times New Roman", serif;
    font-size: 30px;
    letter-spacing: 1px;
    color: var(--brand-blue-dark);
  }
  .letter-body {
    position: absolute;
    left: 60px;
    right: 60px;
    top: 330px;
    font-family: "Tinos", "Times New Roman", serif;
    font-size: 17px;
    line-height: 26px;
    text-align: justify;
    margin: 0;
  }
  .closing {
    position: absolute;
    right: 120px;
    top: 790px;
    text-align: center;
    font-size: 14px;
  }
  .closing .signature {
    display: block;
    margin-top: 10px;
    font-family: "Tinos", "Times New Roman", serif;
    font-size: 14px;
    letter-spacing: 2px;
    color: var(--ink-soft);
  }
  .footer-band {
    position: absolute;
    left: 0;
    bottom: 0;
    width: 858px;
    height: 66px;
    background: var(--brand-blue);
    border-top: 6px solid var(--shadow-grey);
    color: var(--paper);
    font-size: 14px;
    display: flex;
    align-items: center;
    justify-content: center;
    box-sizing: border-box;
  }
</style>
</head>
<body>
<main class="letterhead">
  <svg class="header-band" viewBox="0 0 858 90" aria-hidden="true">
    <polygon points="0,0 858,0 858,30 330,30 270,78 0,78" fill="var(--shadow-grey)"/>
    <polygon points="0,0 858,0 858,22 320,22 262,68 0,68" fill="var(--brand-blue)"/>
  </svg>

  <div class="contact">
    <div class="contact-phone">Ph : +44 141 782 3094</div>
    <div class="contact-email">Email : studio@harborlumenworks.com</div>
  </div>

  <div class="date-line">DATE ..........</div>

  <div class="brand">
    <span class="brand-mark"></span>
    <span class="brand-name">Harbor Lumen Works</span>
  </div>

  <p class="letter-body">She was hurrying along Pennsylvania Avenue, a block from the White House, shivering in the cold December wind, when she heard the terrifying, ear-splitting scream of air-raid sirens and then the sound of a bomber plane overhead, ready to unload its cargo of death. She stopped, frozen, engulfed in a red mist of terror. Suddenly she was back in Sarajevo, and she could hear the shrill whistle of the bombs dropping. She closed her eyes tightly, but it was impossible to shut out the vision of what was happening all around her. The sky was ablaze, and she was deafened by the sounds of automatic-weapons fire, roaring planes, and the wump of deadly mortar shells. Nearby buildings erupted into showers of cement, bricks, and dust. Terrified people were running in every direction, trying to outrace death. From far, far away, a man's voice was saying, 'Are you all right</p>

  <div class="closing">
    yours sincerely
    <span class="signature">HARBOR LUMEN</span>
  </div>

  <footer class="footer-band">47 Thornbury Lane Office 14, Suite #58207, Leeds, West Yorkshire, United Kingdom</footer>
</main>
</body>
</html>
```